Design Tweak needed for a current site

Design on top of an existing quiz funnel

Ideally we would like to tweak what we have already built here (moving elements, styles, adding simple elements etc): http://offers.rateplumfinder.com/could-you-cut-your-auto-premium

The flow:
1) User lands on the quiz page
2) User answers X questions and moves through the flow
3) Calculating user results screen
4) User reaches a success screen, and is subsequently redirected

Keys to the design:
1) We need to emphasize the quiz title as that will drive engagement. In this case, this is a quiz to see if you might be eligible to save money on car insurance.

2) At the end of the quiz we need to make it very, very clear that the user is eligible for savings and that in order to complete the process they are being redirected to another page where they need to fill out a form. It is critical that the design communicates this very clearly... We can count down the time left until redirect and we can use any order of elements to make this point. I think our current design does a very bad job of this.

3) We want to have a "calculating" step so that it seems like the page is working in the background

Goals of the design:
1) Polished, high quality experience throughout
2) User is clearly prepared to be redirected to the conversion funnel/landing page at the end
3) User understands the value of completing the quiz

Target Market(s)

designers

Industry/Entity Type

Moving

Number of Pages Required

1 page

Font styles to use
Sans Serif

Colors

Designer to choose colors to be used in the design.

Requirements
Must have
• This quiz funnel is a template so while the current use case is for auto insurance, we would like a design that also would work in other contexts.
Should not have
• We don't want to materially change the core functionality of the quiz itself... redesigning any of the elements or interactions is encouraged though

```html
<!DOCTYPE html>
<html lang="en">
<head>
<meta charset="utf-8">
<title>RatePlum – Car Insurance Quiz</title>
<link rel="stylesheet" href="https://fonts.googleapis.com/css2?family=Lato:wght@300;700&family=Open+Sans:wght@300;400&display=swap">
<style>
  :root {
    --page-bg: #e9e9eb;
    --white: #ffffff;
    --ink: #1a1a1a;
    --band: #3d3d3d;
    --muted: #8a8a8a;
    --track: #e6e6e6;
    --ring: #ececec;
    --rule: #d9d9d9;
    --black: #000000;
  }
  * { box-sizing: border-box; margin: 0; padding: 0; }
  html, body { width: 1200px; height: 805px; overflow: hidden; }
  body {
    position: relative;
    background: var(--page-bg);
    font-family: "Open Sans", Arial, sans-serif;
    color: var(--ink);
  }
  .site-header {
    position: absolute; left: 0; top: 0; width: 1200px; height: 66px;
    background: var(--white); border-bottom: 1px solid #d6d6d6;
  }
  .brand {
    position: absolute; left: 130px; top: 16px;
    display: flex; align-items: center; gap: 8px;
    font-family: "Open Sans", Arial, sans-serif; font-weight: 400;
    font-size: 24px; color: var(--ink); letter-spacing: 0.3px;
  }
  .brand-dot { width: 22px; height: 22px; border-radius: 50%; background: var(--ink); }

  .quiz-card {
    position: absolute; left: 132px; top: 100px; width: 940px; height: 606px;
    background: var(--white);
  }
  .quiz-banner {
    height: 116px; background: var(--band); color: var(--white);
    text-align: center;
  }
  .quiz-title {
    padding-top: 22px;
    font-family: "Lato", Arial, sans-serif; font-size: 33px; line-height: 40px;
  }
  .quiz-title .label { font-weight: 300; }
  .quiz-title .headline { font-weight: 700; }
  .quiz-subtitle { margin-top: 8px; font-size: 16px; font-weight: 400; }

  .progress { position: absolute; left: 0; top: 116px; width: 940px; height: 110px; }
  .progress-track {
    position: absolute; left: 56px; top: 63px; width: 833px; height: 6px;
    background: var(--track); border: 1px solid #dcdcdc;
  }
  .progress-done {
    position: absolute; left: 56px; top: 63px; width: 60px; height: 5px; background: var(--black);
  }
  .step { position: absolute; top: 37px; width: 80px; margin-left: -40px; text-align: center; }
  .step-dot {
    width: 58px; height: 58px; margin: 0 auto; border-radius: 50%;
    background: var(--ring); border: 1px solid #e0e0e0;
    display: flex; align-items: center; justify-content: center;
  }
  .step-dot svg { width: 26px; height: 26px; stroke: #9a9a9a; fill: none; stroke-width: 1.4; }
  .step-current .step-dot { background: var(--white); border: 5px solid var(--black); width: 58px; height: 58px; }
  .step-current .step-dot svg { stroke: var(--ink); }
  .step-label { margin-top: 6px; font-size: 11px; color: var(--muted); }
  .step-current .step-label { color: var(--ink); }

  .question {
    position: absolute; left: 170px; top: 290px; width: 600px;
    display: flex; align-items: center; gap: 24px;
    font-size: 19px; font-weight: 300; white-space: nowrap;
  }
  .question::before, .question::after { content: ""; flex: 1; height: 1px; background: var(--rule); }

  .choice {
    position: absolute; top: 366px; width: 278px; height: 182px;
    border: 1px solid #e2e2e2; background: var(--white);
    box-shadow: 0 4px 12px rgba(0,0,0,0.07);
    text-align: center;
  }
  .choice-lease { left: 166px; background: var(--black); color: var(--white); border-color: var(--black); }
  .choice-own { left: 493px; }
  .choice-art { width: 72px; height: 72px; margin: 33px auto 0; border-radius: 6px; }
  .choice-lease .choice-art { background: #3a3a3a; }
  .choice-own .choice-art { background: #d8d8d8; }
  .choice-label { margin-top: 18px; font-size: 19px; font-weight: 300; }

  .site-footer {
    position: absolute; left: 0; top: 745px; width: 1200px; text-align: center;
    font-size: 11px; color: #7a7a7a;
  }
</style>
</head>
<body>
  <header class="site-header">
    <div class="brand"><span class="brand-dot"></span>RatePlum</div>
  </header>

  <main class="quiz-card">
    <section class="quiz-banner">
      <h1 class="quiz-title"><span class="label">Quiz: </span><span class="headline">Are You Overpaying For Car Insurance?</span></h1>
      <p class="quiz-subtitle">Take our five question quiz to see if you might be eligible for car insurance savings</p>
    </section>

    <nav class="progress" aria-label="Quiz progress">
      <div class="progress-track"></div>
      <div class="progress-done"></div>
      <div class="step step-current" style="left:137px">
        <div class="step-dot"><svg viewBox="0 0 26 26"><rect x="6" y="4" width="14" height="18"/><path d="M9 9h8M9 12h8M9 15h6M9 19h4"/></svg></div>
        <div class="step-label">Step 1</div>
      </div>
      <div class="step" style="left:292px">
        <div class="step-dot"><svg viewBox="0 0 26 26"><path d="M5 17v-4l3-5h10l3 5v4z"/><circle cx="9" cy="17" r="1.5"/><circle cx="17" cy="17" r="1.5"/></svg></div>
        <div class="step-label">Step 2</div>
      </div>
      <div class="step" style="left:471px">
        <div class="step-dot"><svg viewBox="0 0 26 26"><path d="M4 13a9 9 0 0 1 18 0z"/><path d="M13 13v7a2 2 0 0 1-4 0"/></svg></div>
        <div class="step-label">Step 3</div>
      </div>
      <div class="step" style="left:646px">
        <div class="step-dot"><svg viewBox="0 0 26 26"><path d="M3 18h20M8 8l2 4 3-5 2 5 3-4"/></svg></div>
        <div class="step-label">Step 4</div>
      </div>
      <div class="step" style="left:810px">
        <div class="step-dot"><svg viewBox="0 0 26 26"><path d="M7 14l4 4 8-9"/></svg></div>
        <div class="step-label">Finish</div>
      </div>
    </nav>

    <h2 class="question">Do you Lease or Own</h2>

    <div class="choice choice-lease">
      <div class="choice-art" role="img" aria-label="Illustration of a lease document with a car"></div>
      <div class="choice-label">I Lease</div>
    </div>
    <div class="choice choice-own">
      <div class="choice-art" role="img" aria-label="Illustration of an owner standing beside his car"></div>
      <div class="choice-label">I Own!</div>
    </div>
  </main>

  <footer class="site-footer">Copyrights @ 2017 All Rights Reserved</footer>
</body>
</html>
```